Letterhead design of KESTREL POWER THRIFT INC.

we are a energy saving company doing the solar screen, radian barrier, attic insulation, double panel windows. Basically i need the design of the letterhead including my company name, business address, phone numbers, fax number and email address. Main thing i need it look like a huge company and look like very high class. thanks !!

Reason: Please send me more new design about my company! Thanks so much!!

Industry/Entity Type

Business

```html
<!DOCTYPE html>
<html lang="en">
<head>
<meta charset="utf-8">
<title>Kestrel Power Thrift Inc. – Letterhead</title>
<link href="https://fonts.googleapis.com/css2?family=Arimo:wght@400;700&display=swap" rel="stylesheet">
<style>
  :root {
    --backdrop: #000000;
    --paper: #ffffff;
    --accent-green: #7ac143;
    --accent-orange: #f39a2b;
    --name-grey: #6d6e70;
    --ink: #111111;
  }
  html, body {
    margin: 0;
    padding: 0;
    width: 1200px;
    height: 1008px;
    overflow: hidden;
    background: var(--backdrop);
  }
  .canvas {
    position: relative;
    width: 1200px;
    height: 1008px;
    background: var(--backdrop);
  }
  .letterhead {
    position: absolute;
    left: 196px;
    top: 14px;
    width: 759px;
    height: 984px;
    background: var(--paper);
    overflow: hidden;
  }
  .edge-band {
    position: absolute;
    top: 0;
    right: 0;
    width: 22px;
    height: 100%;
    background: var(--accent-green);
  }
  .brand {
    position: absolute;
    left: 48px;
    top: 50px;
    display: flex;
    align-items: center;
    gap: 16px;
  }
  .brand-dot {
    width: 62px;
    height: 62px;
    border-radius: 50%;
    background: var(--accent-orange);
  }
  .brand-name {
    font-family: "Arimo", Arial, sans-serif;
    font-weight: 700;
    font-size: 34px;
    line-height: 1.05;
    color: var(--name-grey);
    letter-spacing: 0.5px;
  }
  .brand-decoration {
    position: absolute;
    left: 50px;
    top: 560px;
    width: 320px;
    height: 340px;
  }
  .contact {
    position: absolute;
    right: 48px;
    top: 816px;
    font-family: "Arimo", Arial, sans-serif;
    font-size: 13px;
    line-height: 17px;
    color: var(--ink);
    text-align: right;
  }
  .contact p { margin: 0; }
  .contact .company { font-weight: 700; }
  .contact .address { margin-bottom: 16px; }
  .contact .lines { margin-bottom: 16px; }
  .contact .email { text-align: left; }
</style>
</head>
<body>
<div class="canvas">
  <section class="letterhead">
    <div class="edge-band"></div>

    <header class="brand">
      <span class="brand-dot"></span>
      <span class="brand-name">KESTREL<br>POWER THRIFT</span>
    </header>

    <svg class="brand-decoration" role="img" aria-label="Faint brand decoration area in soft orange and green tones" viewBox="0 0 320 340">
      <defs>
        <radialGradient id="soft-tone" cx="45%" cy="45%" r="60%">
          <stop offset="0%" stop-color="#f7c88f" stop-opacity="0.35"/>
          <stop offset="55%" stop-color="#cfe6b4" stop-opacity="0.25"/>
          <stop offset="100%" stop-color="#ffffff" stop-opacity="0"/>
        </radialGradient>
      </defs>
      <rect width="320" height="340" fill="url(#soft-tone)"/>
    </svg>

    <address class="contact">
      <p class="company">Kestrel Power Thrift Inc.</p>
      <div class="address">
        <p>2875 Marlow Park Rd Suite</p>
        <p>#300 Houston, TEXAS 77099</p>
      </div>
      <div class="lines">
        <p>Phone 713-555-0148</p>
        <p>Fax&nbsp; 713-555-0193</p>
      </div>
      <p>Email kestrelpowerthrift@mailbox.com</p>
    </address>
  </section>
</div>
</body>
</html>
```